Health care finance company startup website design

This design brief is for Ledger Loom, a small start-up company dealing with an online health care (initially dental targeted with plans for medical market) financial suite of tools. My business partners and I are looking to have a website developed for our business model.

We have developed a professional logo and would like it incorporated into the site. We are open to modifications on the logo if needed to accomplish the right design.

Our concept is a clean, simple design with a professional polish and very up-to-date web presence. The functionality of the site is simple yet powerful and we would like it’s design to complement that (including anticipated css3/html5 effects for an added dimension of UI polish).

We would like to see a design mockup of the functional elements of our site as our home page. We would also be very interested to see how your design would flow into the other pages such as search for a loan, create a payment plan, make a payment, sign in, registration, contact us and learn more.

Regarding Functional Elements:

-Simplicity is king.

-The three main functions of the site are the focus. They will operate via a series of API’s to webservices on the back-end, making the front end field focused, though we hope to have it feel friendly and simple.
-Search for a loan
-Create a payment plan
-Make a payment

Other functions of the site include:

-Sign in module
-We plan to support Kindred Link, Vortal Verify and PassGate so incorporating design for those options is a plus.

-Registration module
-Two service levels clients can register for, loans only or loans & payments
-The registration process should be divided into sections with navigation back and forth until a confirmation final screen with pdf generations and remaining “to-do items” listed.
-The registration information will be saved in our database and also auto-populate fields for PDF’s that will be generated from templates.
-The registration will send a confirmation email and support PassGate, Vortal Verify and Kindred Link, so designs should take these programmatic features into account.

-Contact us
-This will emphasize digital forms of communication (email and form submitted contact request).

-Learn more
-Explanations/faqs/tutorials
-This will contain video demonstrations/screencasts of key functions of website features

Regarding Design Elements:
-We want to be “wow’d” and don’t mind a surprise that redefines what we thought we liked regarding design.
-The following examples indicate some of the color schemes we like and design elements we hope to incorporate.
-We also recognize there is no substitute for creativity and originality.

Favorite Website Design Examples:

http://www.joggingwithmarla.example/
HD backgrounds are a plus.
These colors are great.
The bright splashes of blue, red and orange combined with black in these shades.
A predominant background of whitesmoke or beige.

https://tillbrook.example/
The HD backgrounds are sharp.
The look is very clean (though it has a slight Pearfield computers imitation).
The left to right “scrolling” is preferable to vertical scrolling.
Very pleasing to the eye.

http://www.gravelpathworks.example/
Again, use of bright, vibrant HD graphics is exceptional.
The left to right scrolling navigation is slick and likely how we would like our services to flow.

http://buzzing.visitlakeshore.example/
Love the look, feel and concepts in this site’s design
Especially colors and “photography” elements.
Updates

We've seen a few common themes in various designs submitted so far and want to add a few suggestions as we enter the final week of our design contest.

We do not want any photos of healthcare professionals or close-ups of people (families or couples or individuals).  Although we are a health care company we don't want to fall into a cliche feel for our site.  Instead we would like either objects or abstract images that have depth and are high definition, spanning from edge to edge of the width of the screen. 

We prefer shades of grey for the base color scheme with highlights of bright colors.  Please refer to the examples on the brief and use those as the best guide of what we want.  Even SketchHive's color scheme is closer to what we want than some of the submissions, so please take note of the "shades of grey" with splashes of bright accent colors.

We love the horizontal navigation bar like that seen in the gravel-path works site and anticipate our final product using a similar transition between the functions of the site.

Good luck to you all.  We are still looking for that WOW factor and hoping to see something original, that breaks the traditional mold and has a feel like the examples posted.  

Industry/Entity Type

Communication

```html
<!DOCTYPE html>
<html lang="en">
<head>
<meta charset="utf-8">
<title>Health Care – Home</title>
<link rel="stylesheet" href="https://fonts.googleapis.com/css2?family=Oswald:wght@400;500&family=Arimo:ital,wght@0,400;0,700;1,400&display=swap">
<style>
:root{
  --red:#d64848;
  --red-dark:#b93434;
  --red-soft:rgba(214,72,72,.88);
  --red-deep:rgba(190,50,52,.92);
  --logo-pale:#e39c9a;
  --ink:#222;
  --grey-text:#8a8a8a;
  --grey-line:#d6d6d6;
  --page:#ebebeb;
  --footer:#f6f6f6;
  --white:#fff;
}
*{box-sizing:border-box;margin:0;padding:0}
html,body{width:1141px;height:1200px;overflow:hidden}
body{position:relative;background:var(--page);font-family:"Arimo",Arial,sans-serif;color:var(--ink)}
.abs{position:absolute}
.top-rule{left:0;top:0;width:1141px;height:6px;background:var(--red);z-index:3}
.hero-photo{left:0;top:0;width:1141px;height:860px;
  background:
   radial-gradient(ellipse 320px 260px at 1050px 180px,rgba(150,190,90,.55),transparent 70%),
   radial-gradient(ellipse 260px 300px at 700px 420px,rgba(90,190,110,.45),transparent 70%),
   radial-gradient(ellipse 240px 260px at 300px 260px,rgba(238,196,160,.75),transparent 70%),
   radial-gradient(ellipse 260px 280px at 880px 330px,rgba(220,160,125,.7),transparent 70%),
   radial-gradient(ellipse 200px 200px at 560px 300px,rgba(230,180,150,.6),transparent 70%),
   linear-gradient(180deg,#f4efe9 0%,#efe4da 45%,#efe9e6 75%,var(--page) 100%)}
.logo{left:447px;top:6px;width:247px;height:72px;background:var(--red);display:flex;align-items:center;justify-content:center;gap:10px;z-index:2}
.logo .mark{width:16px;height:16px;background:var(--white)}
.logo .name{font-family:"Oswald",sans-serif;font-weight:500;font-size:36px;color:var(--white);line-height:1}
.main-nav{left:378px;top:78px;width:382px;height:33px;background:rgba(255,255,255,.82);display:flex;justify-content:space-around;align-items:center;font-family:"Oswald",sans-serif;font-size:13px}
.main-nav a{color:var(--red);text-decoration:none}
.main-nav a.current{color:var(--ink);border-bottom:2px solid var(--ink);padding-bottom:2px}
.slide-next{left:1017px;top:248px;width:52px;height:52px;border-radius:50%;background:rgba(255,255,255,.45)}
.features{left:168px;top:530px;width:805px;height:114px;display:flex;border-radius:4px;overflow:hidden}
.feature{flex:1;background:var(--red-soft);display:flex;align-items:center;padding:0 18px;gap:18px;color:var(--white)}
.feature.active{background:var(--red-deep)}
.feature svg{flex:none}
.feature h3{font-family:"Oswald",sans-serif;font-weight:400;font-size:16px;margin-bottom:4px}
.feature p{font-size:10px;line-height:1.35}
.section-title{font-family:"Oswald",sans-serif;font-weight:400;font-size:19px;color:var(--ink)}
.section-title em{font-style:normal;color:var(--red)}
.welcome-photo{left:184px;top:690px;width:235px;height:141px;background:linear-gradient(135deg,#8ec9c7,#d8ecec 55%,#e9d2c4)}
.welcome-copy{left:184px;top:838px;width:240px;font-size:10px;line-height:1.45;color:var(--grey-text)}
.welcome-copy p+p{margin-top:12px}
.divider{left:437px;top:652px;width:1px;height:350px;background:var(--grey-line)}
.testimonial{left:466px;top:696px;width:496px}
.testimonial .meta{display:flex;justify-content:space-between;font-size:10px;padding:6px 0;border-bottom:1px solid var(--grey-line)}
.testimonial .meta b em{font-style:normal;color:var(--red)}
.testimonial .meta span{color:var(--grey-text);font-style:italic}
.testimonial blockquote{font-style:italic;font-size:9.5px;line-height:1.45;color:var(--grey-text);padding:8px 0;border-bottom:1px solid var(--grey-line)}
.dots{left:466px;top:808px;display:flex;gap:4px}
.dots i{width:5px;height:5px;border-radius:50%;background:#bbb}
.dots i:first-child{background:var(--red)}
.btn-red{background:var(--red);color:var(--white);font-size:10px;border-radius:3px;display:flex;align-items:center;justify-content:center}
.all-testimonials{left:852px;top:799px;width:102px;height:18px}
.partners{left:458px;top:883px;width:504px;height:84px;background:var(--white);border:1px solid var(--grey-line);display:flex;align-items:center;justify-content:space-between;padding:0 8px}
.partners ul{list-style:none;display:flex;gap:22px;align-items:center}
.partners li{display:flex;align-items:center;gap:6px;font-size:11px;font-weight:700;color:#444}
.partners li i{width:14px;height:14px;background:#888;border-radius:50%}
.arrow-btn{width:18px;height:18px;border-radius:50%;background:#111}
.site-footer{left:0;top:1055px;width:1141px;height:137px;background:var(--footer);border-top:1px solid #ddd}
.bottom-rule{left:0;top:1192px;width:1141px;height:8px;background:var(--red)}
.footer-title{font-family:"Oswald",sans-serif;font-weight:400;font-size:15px;color:var(--ink)}
.footer-links{list-style:none;font-size:9.5px;color:#777;line-height:16.5px}
.email-field{left:416px;top:1105px;width:228px;height:22px;background:var(--white);border:1px solid #ccc;font-size:9.5px;font-style:italic;color:#999;padding:5px 6px}
.subscribe-btn{left:416px;top:1138px;width:101px;height:21px;font-size:11px}
.subscribe-note{left:523px;top:1137px;font-size:9px;line-height:1.45;color:#888;width:110px}
.footer-logo{left:803px;top:1079px;width:155px;height:47px;background:var(--logo-pale);display:flex;align-items:center;justify-content:center;gap:7px}
.footer-logo .mark{width:11px;height:11px;background:var(--white)}
.footer-logo .name{font-family:"Oswald",sans-serif;font-weight:500;font-size:23px;color:var(--white)}
.copyright{left:700px;top:1137px;width:258px;text-align:right;font-size:9px;color:#777}
</style>
</head>
<body>
<div class="abs top-rule"></div>
<div class="abs hero-photo" role="img" aria-label="Hero photograph: a smiling family hugging outdoors in bright sunlight, softly fading into the page"></div>

<div class="abs logo"><span class="mark"></span><span class="name">Health Care</span></div>
<nav class="abs main-nav">
  <a class="current" href="#">Home</a><a href="#">About Us</a><a href="#">Payment Plan</a><a href="#">Partners</a><a href="#">Contact Us</a>
</nav>
<div class="abs slide-next"><svg width="52" height="52" viewBox="0 0 52 52"><path d="M22 16l10 10-10 10" fill="none" stroke="#fff" stroke-width="4"/></svg></div>

<section class="abs features">
  <div class="feature">
    <svg width="52" height="52" viewBox="0 0 52 52"><circle cx="21" cy="21" r="13" fill="none" stroke="#fff" stroke-width="5"/><path d="M31 31l14 14" stroke="#fff" stroke-width="7" stroke-linecap="round"/></svg>
    <div><h3>Search For a Loan</h3><p>Lorem Ipsum is simply dummy text of the printing and typesetting industry.</p></div>
  </div>
  <div class="feature active">
    <svg width="52" height="52" viewBox="0 0 52 52"><rect x="4" y="10" width="40" height="26" rx="2" fill="#e58a88"/><rect x="8" y="18" width="40" height="26" rx="2" fill="#fff"/><rect x="8" y="23" width="40" height="4" fill="#c44"/><rect x="14" y="33" width="22" height="3" fill="#c44"/></svg>
    <div><h3>Create a Payment Plan</h3><p>Lorem Ipsum is simply dummy text of the printing and typesetting industry.</p></div>
  </div>
  <div class="feature">
    <svg width="52" height="52" viewBox="0 0 52 52"><circle cx="26" cy="26" r="22" fill="none" stroke="#fff" stroke-width="4"/><text x="26" y="36" text-anchor="middle" font-family="Arimo,sans-serif" font-weight="700" font-size="28" fill="#fff">$</text></svg>
    <div><h3>Make a Payment</h3><p>Lorem Ipsum is simply dummy text of the printing and typesetting industry.</p></div>
  </div>
</section>

<h2 class="abs section-title" style="left:181px;top:656px">Welcome to <em>Health Care</em></h2>
<div class="abs welcome-photo" role="img" aria-label="Photograph of a dental check-up in a bright clinic"></div>
<div class="abs welcome-copy">
  <p>Lorem ipsum dolor sit amet, consectetur adipiscing elit. Sed posuere diam quis turpis varius fermentum in in ipsum. Morbi eget quam vitae nisl consectetur sodales facilisis at ipsum. Sed id justo libero. Sed vestibulum tincidunt ultrices. Duis accumsan velit porttitor ipsum fringilla pretium.</p>
  <p>Pellentesque faucibus aliquet consectetur. Ut tempor bibendum rutrum. Mauris ut neque et lacus fringilla ullamcorper dignissim in sem.</p>
</div>
<div class="abs divider"></div>

<h2 class="abs section-title" style="left:458px;top:656px">What Our <em>Customers Say</em></h2>
<article class="abs testimonial">
  <div class="meta"><b>Owen Castell, <em>Manager.</em></b><span>Posted : 27 Jan, 2012 &nbsp;|&nbsp; 20:15 am</span></div>
  <blockquote>Lorem ipsum dolor sit amet, consectetur adipiscing elit. Sed posuere diam quis turpis varius fermentum in in ipsum. Morbi eget quam vitae nisl consectetur sodales facilisis at ipsum. Sed id justo libero. Sed vestibulum tincidunt ultrices. Duis accumsan velit porttitor ipsum fringilla pretium. Pellentesque faucibus aliquet consectetur. Ut tempor bibendum rutrum. Mauris ut neque et lacus fringilla ullamcorper dignissim in sem.</blockquote>
</article>
<div class="abs dots"><i></i><i></i><i></i><i></i><i></i></div>
<a class="abs btn-red all-testimonials">view all testimonials</a>

<h2 class="abs section-title" style="left:458px;top:846px">Our <em>Business Partners</em></h2>
<div class="abs partners">
  <svg class="arrow-btn" viewBox="0 0 18 18"><circle cx="9" cy="9" r="9"/><path d="M11 5l-4 4 4 4" fill="none" stroke="#fff" stroke-width="2"/></svg>
  <ul>
    <li><i></i>Ridgeview Clinic</li>
    <li><i></i>Alderbank Hospital</li>
    <li><i></i>Vitacore S.A.</li>
    <li><i></i>Parish Hospital</li>
  </ul>
  <svg class="arrow-btn" viewBox="0 0 18 18"><circle cx="9" cy="9" r="9"/><path d="M7 5l4 4-4 4" fill="none" stroke="#fff" stroke-width="2"/></svg>
</div>

<footer class="abs site-footer"></footer>
<h3 class="abs footer-title" style="left:181px;top:1076px">About Us</h3>
<ul class="abs footer-links" style="left:181px;top:1102px"><li>Company Info</li><li>Search Loan</li><li>Services</li><li>Clients</li></ul>
<ul class="abs footer-links" style="left:284px;top:1102px"><li>Payment Plan</li><li>Partners</li><li>Contact Us</li><li>Terms &amp; Privacy</li></ul>
<h3 class="abs footer-title" style="left:416px;top:1076px">Subscribe Newsletter</h3>
<div class="abs email-field">Email Address</div>
<a class="abs btn-red subscribe-btn">Subscribe Now</a>
<p class="abs subscribe-note">Free Subscribe our latest offers and Plans.</p>
<div class="abs footer-logo"><span class="mark"></span><span class="name">Health Care</span></div>
<p class="abs copyright">Copy © Health Care. All rights reserved.</p>
<div class="abs bottom-rule"></div>
</body>
</html>
```